Banner Design 4040mm W x 2190mm H

Design a glamorous and exciting 4040mm W x 2190mm H backdrop for the QRLMT Velvet Orchid Gala at the luxurious Tallow Hall, Fenwick, Mirrabelle, Sydney. This exciting backdrop should be spectacular so that people will be excited to take photos in front of it.
Design Colours preferred is black and pink.
Please include our website on the banner www.qrlmt.org.au
Should include the words "QRLMT Velvet Orchid Gala" as the main attraction on the banner.
Please include "Thank you to our sponsors" and include the logo of the sponsors.
Sponsors:
Brockden Pathology
EastGlen Radiology
KTV Diagnostic Imaging
Harbin Legal Group
Truffords
Banner Template:
4040mm W x 2190mm H Single Sided (.AI)
https://files.example-share.net/d/8ZkQm3TnWp47LcVbXr2YhJd5Fs61Ae/view
QRLMT Logo:
Can be obtained from our website www.qrlmt.org.au

```html
<!DOCTYPE html>
<html lang="en">
<head>
<meta charset="utf-8">
<title>QRLMT Velvet Orchid Gala – Sponsor Backdrop</title>
<link rel="stylesheet" href="https://fonts.googleapis.com/css2?family=Great+Vibes&family=Montserrat:wght@400;600&display=swap">
<style>
  :root {
    --page-bg: #d3d3d3;
    --backdrop-black: #050005;
    --deep-plum: #3a0038;
    --glow-magenta: #c21cc0;
    --wing-pink: #e04fe0;
    --bokeh-pink: #a8139f;
    --text-white: #ffffff;
    --sponsor-ink: #1d2a5c;
    --sponsor-card: #ffffff;
  }
  * { margin: 0; padding: 0; box-sizing: border-box; }
  html, body {
    width: 1121px;
    height: 1200px;
    overflow: hidden;
    background: var(--page-bg);
  }
  .backdrop {
    position: absolute;
    left: 40px;
    top: 318px;
    width: 1041px;
    height: 564px;
    overflow: hidden;
    background:
      radial-gradient(ellipse 48% 60% at 50% 42%, var(--deep-plum) 0%, rgba(58,0,56,0.4) 55%, transparent 80%),
      var(--backdrop-black);
    font-family: "Montserrat", sans-serif;
    color: var(--text-white);
  }
  .bokeh-glow {
    position: absolute;
    left: 0; right: 0; bottom: 0;
    height: 260px;
    background:
      radial-gradient(ellipse 30% 70% at 0% 100%, var(--bokeh-pink) 0%, transparent 75%),
      radial-gradient(ellipse 30% 70% at 100% 100%, var(--bokeh-pink) 0%, transparent 75%),
      linear-gradient(to top, rgba(168,19,159,0.55), transparent);
  }
  .wings-art {
    position: absolute;
    left: 195px;
    top: 64px;
    width: 650px;
    height: 360px;
    border-radius: 48% 48% 40% 40% / 30% 30% 70% 70%;
    background:
      radial-gradient(ellipse 50% 55% at 50% 55%, var(--wing-pink) 0%, var(--glow-magenta) 50%, rgba(194,28,192,0) 100%);
    box-shadow: 0 0 60px 10px rgba(194,28,192,0.45);
  }
  .org-mark {
    position: absolute;
    left: 38px;
    top: 40px;
    width: 150px;
    text-align: center;
  }
  .org-mark__dot {
    width: 96px;
    height: 96px;
    margin: 0 auto 22px;
    border-radius: 50%;
    background: var(--text-white);
  }
  .org-mark__name {
    font-weight: 400;
    font-size: 19px;
    letter-spacing: 0.5px;
  }
  .headline {
    position: absolute;
    left: 300px;
    width: 440px;
    text-align: center;
  }
  .headline__thanks {
    top: 30px;
    font-family: "Great Vibes", cursive;
    font-size: 80px;
    line-height: 1;
  }
  .headline__sponsors {
    top: 114px;
    font-size: 17px;
    font-weight: 400;
    letter-spacing: 0.3px;
  }
  .event-title {
    position: absolute;
    left: 371px;
    top: 160px;
    width: 300px;
    text-align: center;
    font-family: "Great Vibes", cursive;
    font-size: 46px;
    line-height: 42px;
  }
  .sponsor-row {
    position: absolute;
    top: 467px;
    height: 48px;
    left: 277px;
    display: flex;
    gap: 13px;
  }
  .sponsor-card {
    height: 48px;
    width: 90px;
    border-radius: 4px;
    background: var(--sponsor-card);
    display: flex;
    align-items: center;
    justify-content: center;
    text-align: center;
    font-weight: 600;
    font-size: 10px;
    line-height: 1.15;
    color: var(--sponsor-ink);
  }
  .sponsor-card--narrow { width: 73px; }
</style>
</head>
<body>
  <main class="backdrop">
    <div class="bokeh-glow" role="img" aria-label="Soft pink bokeh light particles along the bottom"></div>
    <div class="wings-art" role="img" aria-label="Glowing pink angel wings illustration"></div>

    <div class="org-mark">
      <div class="org-mark__dot"></div>
      <div class="org-mark__name">QRLMT</div>
    </div>

    <h1 class="headline headline__thanks">Thank you</h1>
    <p class="headline headline__sponsors">to our sponsors</p>

    <h2 class="event-title">Velvet<br>Orchid<br>Gala</h2>

    <ul class="sponsor-row" style="list-style:none">
      <li class="sponsor-card">Brockden<br>Pathology</li>
      <li class="sponsor-card">KTV Diagnostic<br>Imaging</li>
      <li class="sponsor-card sponsor-card--narrow">Truffords</li>
      <li class="sponsor-card">EastGlen<br>Radiology</li>
      <li class="sponsor-card">Harbin<br>Legal Group</li>
    </ul>
  </main>
</body>
</html>
```